Product Introduction Brochure

Brochure to introduce our mid/high end lighting products to potential wholesalers / Disrtibutors / Retailers. To be mainly graphical but will contain some text also. The purpose of the brochure will be to get potential customers to find out more either by calling us or to visit our website. The brochure should be of A3 size folded in half to an A4. Front page should be mainly logo and name, inner 2 pages should showcase some of the products we can supply together with some text (to be supplied, please use filler text in the initial design), then the back page containing our contact details. The products are lights, floor lamps and table lamps. I have attached a number of images, as well as our company logo. I would prefer the design to be on a black background, however this is not critical
Target Market(s)
Retailer, distribution and wholesale buyers
Interior design consultants and specifiers
Industry/Entity Type
Product
Look and feel
Each slider illustrates characteristics of the customer's brand and the style your logo design should communicate.

```html
<!DOCTYPE html>
<html lang="en">
<head>
<meta charset="utf-8">
<title>Lumora Lighting Brochure</title>
<link rel="stylesheet" href="https://fonts.googleapis.com/css2?family=Questrial&family=Roboto+Condensed:wght@400&family=Playfair+Display:ital,wght@1,700&display=swap">
<style>
  :root {
    --stage: #e9e6e1;
    --black: #050505;
    --green: #27b04a;
    --green-dark: #076a35;
    --white: #ffffff;
    --grey-text: #d9d9d9;
  }
  * { box-sizing: border-box; margin: 0; padding: 0; }
  html, body { width: 1200px; height: 900px; overflow: hidden; }
  body { background: var(--stage); position: relative; font-family: "Roboto Condensed", sans-serif; }

  .page {
    position: absolute;
    top: 80px;
    width: 530px;
    height: 740px;
    background: var(--black);
    overflow: hidden;
    box-shadow: 0 8px 24px rgba(0,0,0,.25);
  }
  .page--back { left: 50px; }
  .page--front { left: 620px; }

  /* Back page */
  .pendant-photo {
    position: absolute; left: 40px; top: 20px; width: 230px; height: 260px;
    background: radial-gradient(ellipse at 50% 55%, #d8d8d8 0%, #8f8f8f 35%, #1a1a1a 75%, var(--black) 100%);
  }
  .about {
    position: absolute; left: 235px; top: 292px; width: 270px; color: var(--grey-text);
  }
  .about__title { font-family: "Questrial", sans-serif; font-size: 14px; font-weight: 400; color: var(--white); margin-bottom: 2px; }
  .about__text { font-size: 10px; line-height: 12px; text-align: justify; margin-bottom: 10px; }
  .brand--back {
    position: absolute; left: 150px; top: 590px; display: flex; align-items: center; gap: 14px;
  }
  .brand__dot { width: 68px; height: 68px; border-radius: 50%; background: var(--green); }
  .brand__name { font-family: "Questrial", sans-serif; font-size: 48px; color: var(--green); line-height: 1; }
  .contact-band {
    position: absolute; left: 0; bottom: 0; width: 100%; height: 70px; background: var(--green);
    display: flex; flex-direction: column; justify-content: center; align-items: center;
    font-size: 13px; line-height: 16px; color: var(--black);
  }

  /* Front page */
  .brand--front {
    position: absolute; left: 0; top: 35px; width: 100%; display: flex; justify-content: center; align-items: center; gap: 12px;
  }
  .brand--front .brand__dot { width: 62px; height: 62px; }
  .brand--front .brand__name { font-size: 40px; }
  .rule { position: absolute; left: 0; width: 100%; height: 2px; background: var(--white); }
  .rule--top { top: 140px; }
  .rule--bottom { top: 562px; }
  .hero { position: absolute; left: 0; top: 145px; width: 530px; height: 415px; }
  .slogan {
    position: absolute; left: 30px; top: 262px; width: 110px;
    font-family: "Playfair Display", serif; font-style: italic; font-weight: 700;
    font-size: 26px; line-height: 34px; color: var(--white);
  }
  .slogan span { display: block; }
  .footer-band {
    position: absolute; left: 0; top: 568px; width: 100%; height: 172px; background: var(--green-dark);
    display: flex; justify-content: center; align-items: center;
  }
  .website { font-family: "Playfair Display", serif; font-style: italic; font-weight: 700; font-size: 15px; color: var(--white); }
</style>
</head>
<body>

<section class="page page--back">
  <div class="pendant-photo" role="img" aria-label="Photo of three white pendant lamps hanging on chrome fittings"></div>

  <div class="about">
    <h2 class="about__title">About Us</h2>
    <p class="about__text">Lorem ipsum dolor sit amet, consectetur adipiscing elit, sed do eiusmod tempor incididunt ut labore et dolore magna aliqua. Ut enim ad minim veniam, quis nostrud exercitation ullamco laboris nisi ut aliquip ex ea commodo consequat. Duis aute irure dolor in reprehenderit in voluptate velit esse cillum dolore eu fugiat nulla pariatur. Excepteur sint occaecat cupidatat non proident, sunt in culpa qui officia deserunt mollit anim id est laborum. Sed ut perspiciatis unde omnis iste natus error sit voluptatem accusantium.</p>
    <p class="about__text">Nemo enim ipsam voluptatem quia voluptas sit aspernatur aut odit aut fugit, sed quia consequuntur magni dolores eos qui ratione voluptatem sequi nesciunt. Neque porro quisquam est, qui dolorem ipsum quia dolor sit amet, consectetur, adipisci velit, sed quia non numquam eius modi tempora incidunt ut labore et dolore magnam aliquam quaerat voluptatem. Ut enim ad minima veniam, quis nostrum exercitationem ullam corporis suscipit laboriosam, nisi ut aliquid ex ea commodi consequatur. Quis autem vel eum iure reprehenderit qui in ea voluptate velit esse quam nihil molestiae consequatur, vel illum qui dolorem eum fugiat quo voluptas nulla pariatur.</p>
  </div>

  <div class="brand brand--back">
    <span class="brand__dot"></span>
    <span class="brand__name">Lumora</span>
  </div>

  <div class="contact-band">
    <span>Suite 0000, Street Name, Area Name, City Name, Countr code.</span>
    <span>Contact Us : +123 456 789 | Email : hello@lumoralights.com</span>
    <span>Log On : www.lumoralights.com</span>
  </div>
</section>

<section class="page page--front">
  <div class="brand brand--front">
    <span class="brand__dot"></span>
    <span class="brand__name">Lumora</span>
  </div>
  <div class="rule rule--top"></div>

  <svg class="hero" viewBox="0 0 530 415" width="530" height="415">
    <defs>
      <radialGradient id="photoGlow" cx="65%" cy="45%" r="60%">
        <stop offset="0%" stop-color="#6b7176"/>
        <stop offset="60%" stop-color="#2a2d30"/>
        <stop offset="100%" stop-color="#141516"/>
      </radialGradient>
    </defs>
    <rect x="180" y="0" width="350" height="415" fill="url(#photoGlow)" role="img" aria-label="Photo of a chrome table lamp with a white drum shade on a dark side table"/>
    <path d="M215,0 C300,50 255,150 262,230 C268,310 285,370 315,415" fill="none" stroke="#050505" stroke-width="14"/>
    <path d="M0,0 L200,0 C285,55 238,150 246,232 C252,315 270,372 300,415 L0,415 Z" fill="#27b04a"/>
  </svg>
  <p class="slogan"><span>Put</span><span>Your</span><span>Slogan</span><span>here</span></p>

  <div class="rule rule--bottom"></div>
  <div class="footer-band">
    <span class="website">www.lumoralights.com</span>
  </div>
</section>

</body>
</html>
```